Opening Soon Hoarding Design for Retail Footwear Chain

TREVALLO is a retail footwear chain operating primarily in North America. It offers exclusive and non-exclusive brands for men and women.

We need an advertisement design announcing a store opening, to be placed on a hoarding.

A hoarding is a large board in an enclosed shopping center, used to display advertisements; similar to a billboard. It is a temporary board (or fence) erected in front of a retail site during the construction period.

The advertisement we need is to be placed on the hoarding that covers the store front facade during the construction period, and it is removed the night prior to opening day.

Attached are the TREVALLO store pictures, as well as the logo / pantone color document. The primary colors identifying TREVALLO are Rose gold, white, and red.

The objective or focus of the advertisement on the hoarding should include the following:
- TREVALLO (as per logo)
- Opening soon
- website : www.trevallo-example.ca
- Facebook / Twitter
- A clearly identified section of the advertisement announcing that we are recruiting / looking for employees; this should be announced as: "Join the Trevallo Family" and provide email: careers@trevallo-example.ca

Target Market(s)

Women & men between the approx ages of 25 to 65. The age group is quite wide because the product range we have in the store is very diverse too.

Industry/Entity Type

Retail

Requirements
Must have
• 1- Trevallo name / logo
• 2- Opening soon
• 3- website: www.trevallo-example.ca (& Facebook / twitter reference)
• 4- Join the Trevallo Family: careers@trevallo-example.ca
• Main objective: To have a design that will intrigue people walking in a shopping mall enough for them to stop for a second and look at the ad design. (At the end of the day, that's the main objective of a hoarding design - to get people's attention).
Nice to have
• I can give you an approx. SIZE, but I would like a design that can be slightly modified for printing purposes, as the hoarding size from 1 store to the next will not be identical. However, I would like to use the same design for all hoardings.
• With that said, the approx hoarding size would be 15 feet wide and 10 feet high.
• Some other hoardings will be slightly bigger in width (going up to 20 ft max) but the height should be fairly standard.
Should not have
• The end design should not have a picture / design of the store as per the attached images. The store design and how it looks should be a surprise for the customers.

```html
<!DOCTYPE html>
<html lang="en">
<head>
<meta charset="utf-8">
<title>Trevallo – Opening Soon Hoarding</title>
<link rel="stylesheet" href="https://fonts.googleapis.com/css2?family=Cinzel:wght@700&family=Questrial&display=swap">
<style>
  :root {
    --stage: #1c1c1c;
    --slate: #9a9c9e;
    --cream: #e9e7e2;
    --brand-red: #a81f24;
    --band-red: #620005;
    --band-rule: #c8202a;
    --white: #ffffff;
  }
  * { margin: 0; padding: 0; box-sizing: border-box; }
  html, body {
    width: 1200px;
    height: 1000px;
    overflow: hidden;
    background: var(--stage);
  }
  .hoarding {
    position: absolute;
    left: 170px;
    top: 212px;
    width: 860px;
    height: 575px;
    overflow: hidden;
    background: var(--slate);
  }
  .hoarding__backdrop {
    position: absolute;
    inset: 0;
    width: 860px;
    height: 575px;
  }
  .hoarding__content {
    position: absolute;
    inset: 0;
    text-align: center;
    color: var(--white);
  }
  .brand-name {
    position: absolute;
    left: 0; right: 0;
    top: 74px;
    font-family: "Questrial", sans-serif;
    font-size: 34px;
    letter-spacing: 6px;
    line-height: 40px;
  }
  .headline-band {
    position: absolute;
    left: 92px;
    width: 744px;
    top: 134px;
    height: 82px;
    background: var(--band-red);
    border-top: 1px dotted var(--band-rule);
    border-bottom: 1px dotted var(--band-rule);
  }
  .headline {
    position: absolute;
    left: 0; right: 0;
    top: 134px;
    height: 82px;
    font-family: "Cinzel", serif;
    font-weight: 700;
    font-size: 70px;
    line-height: 84px;
    letter-spacing: 1px;
    margin-left: 25px;
  }
  .website {
    position: absolute;
    left: 0; right: 0;
    top: 230px;
    font-family: "Cinzel", serif;
    font-weight: 700;
    font-size: 29px;
    line-height: 40px;
    margin-left: 25px;
  }
  .social {
    position: absolute;
    top: 290px;
    left: 369px;
    display: flex;
    gap: 28px;
  }
  .social__circle {
    width: 48px;
    height: 48px;
    border: 1.5px solid var(--white);
    border-radius: 50%;
  }
  .recruiting {
    position: absolute;
    left: 0; right: 0;
    top: 480px;
    font-family: "Questrial", sans-serif;
    font-size: 24px;
    line-height: 31px;
    margin-left: 25px;
  }
</style>
</head>
<body>
  <main class="hoarding">
    <svg class="hoarding__backdrop" viewBox="0 0 860 575" aria-hidden="true">
      <ellipse class="outer-ring" cx="430" cy="290" rx="428" ry="470" fill="var(--cream)"/>
      <path class="ring-groove-left" d="M30 0 C-40 170 -20 430 110 575 L90 575 C-30 430 -50 170 12 0 Z" fill="var(--slate)"/>
      <path class="ring-groove-right" d="M830 0 C900 170 880 430 750 575 L770 575 C890 430 910 170 848 0 Z" fill="var(--slate)"/>
      <ellipse class="red-disc" cx="432" cy="290" rx="392" ry="420" fill="var(--brand-red)"/>
      <path class="blade-left" d="M90 200 C55 320 65 430 100 480 C80 410 80 300 90 200 Z" fill="var(--cream)"/>
      <path class="blade-right" d="M780 200 C815 320 805 430 770 480 C790 410 790 300 780 200 Z" fill="var(--cream)"/>
    </svg>

    <div class="hoarding__content">
      <p class="brand-name">TREVALLO</p>
      <div class="headline-band"></div>
      <h1 class="headline">OPENING SOON</h1>
      <p class="website">WWW.TREVALLO-EXAMPLE.CA</p>
      <div class="social" aria-label="Social media links">
        <span class="social__circle"></span>
        <span class="social__circle"></span>
      </div>
      <p class="recruiting">Join the Trevallo Family<br>careers@trevallo-example.ca</p>
    </div>
  </main>
</body>
</html>
```